Classic, clean, and fun community pool party door hangers

Looking for a classy, but FUn door hangers for a community outreach pool party.
While we are a faith-based organization, we do NOT want this to look religious.
RGB Color # 4c7991
Template included

Target Market(s)

Families

Font styles to use
Sans Serif

Colors
f37122
959595
dbdbdb

Requirements
Must have
• Date: July 26, 2018 Thursday
• Time: 5:30pm - 7:30pm MDT
• Location: Marbeck Pool: 2849 7th St NE, Loveland, CO 80538
• Free food while it lasts, games, prizes, swimming, and raffle
Should not have
• No Religious symbols

```html
<!DOCTYPE html>
<html lang="en">
<head>
<meta charset="utf-8">
<title>Riverstone Church Community Pool Party Door Hanger</title>
<link href="https://fonts.googleapis.com/css2?family=Poppins:wght@400;600;700;800&display=swap" rel="stylesheet">
<style>
  :root {
    --page-bg: #ecebe8;
    --deep-blue: #3457a8;
    --pool-blue: #27a3dc;
    --pale-blue: #bfe6f7;
    --sunny-yellow: #f4d10f;
    --white: #ffffff;
  }
  * { margin: 0; padding: 0; box-sizing: border-box; }
  html, body {
    width: 1200px; height: 1000px; overflow: hidden;
    background: var(--page-bg);
    font-family: "Poppins", Arial, sans-serif;
  }
  .door-hanger {
    position: absolute; left: 430px; top: 70px;
    width: 340px; height: 860px;
    background: var(--deep-blue);
    overflow: hidden;
  }
  .hanger-cutout { position: absolute; left: 0; top: 0; }
  .perks {
    position: absolute; left: 30px; right: 20px; top: 22px;
    color: var(--sunny-yellow); font-weight: 700; font-size: 13.5px;
    line-height: 1.3; text-align: center;
  }
  .event-title {
    position: absolute; left: 0; right: 0; top: 218px;
    text-align: center; font-weight: 800; font-size: 40px;
    line-height: 0.98; letter-spacing: 0.3px; text-transform: uppercase;
  }
  .event-title .host { color: var(--white); display: block; }
  .event-title .event { color: var(--sunny-yellow); display: block; }
  .pool-section {
    position: absolute; left: 0; right: 0; top: 385px; bottom: 0;
    background: var(--pool-blue);
  }
  .pool-wave { position: absolute; left: 0; top: -8px; }
  .event-when {
    position: absolute; left: 0; right: 0; top: 42px;
    text-align: center; color: var(--pale-blue);
    font-weight: 700; font-size: 22px; line-height: 1.35;
  }
  .swimmer-art {
    position: absolute; left: 0; right: 0; top: 110px; height: 265px;
    background: radial-gradient(ellipse at 50% 50%, #f3c9b8 0%, #bfe6f7 40%, #27a3dc 100%);
  }
  .venue {
    position: absolute; left: 0; right: 0; bottom: 0; height: 105px;
    background: var(--sunny-yellow);
    display: flex; align-items: center; justify-content: center;
    text-align: center; color: var(--deep-blue);
    font-weight: 400; font-size: 18px; line-height: 1.4;
  }
</style>
</head>
<body>
  <div class="door-hanger">
    <svg class="hanger-cutout" width="340" height="240" viewBox="0 0 340 240" aria-hidden="true">
      <path d="M0 95 Q40 95 70 112 L120 140 L120 172 L60 172 Q30 172 0 186 Z" fill="var(--page-bg)"/>
      <circle cx="170" cy="150" r="58" fill="var(--page-bg)"/>
    </svg>
    <p class="perks">Free food (while it lasts!) Free games, prizes, swimming, and raffle.</p>
    <h1 class="event-title">
      <span class="host">Riverstone<br>Church</span>
      <span class="event">Community<br>Pool Party</span>
    </h1>
    <section class="pool-section">
      <svg class="pool-wave" width="340" height="20" viewBox="0 0 340 20" aria-hidden="true">
        <path d="M0 8 Q20 2 40 9 T80 8 T120 9 T160 7 T200 9 T240 8 T280 9 T320 7 T340 8 L340 20 L0 20 Z" fill="var(--pool-blue)"/>
      </svg>
      <p class="event-when">THURSDAY 07 | 26 | 2018<br>5:30pm - 7:30pm MDT</p>
      <div class="swimmer-art" role="img" aria-label="Illustration of a child in goggles and a yellow swimsuit swimming in a blue pool"></div>
      <div class="venue"><p>Marbeck Pool: 2849 7th St NE,<br>Loveland, CO 80538</p></div>
    </section>
  </div>
</body>
</html>
```